Salt Water Delivery Company Business Card Design

We are a company that delivers natural saltwater (from the ocean) to aquarium companies, restaurants and home marine tanks. I would like a new business card to suit.

Must include Name, company name, abn, contact number and website as well as logo (see attached).

Looking for a design that stands out, has a clean but unique appearance.

Double and single sided entries welcome

Industry/Entity Type

Business

Requirements
Must have
• Logo

```html
<!DOCTYPE html>
<html lang="en">
<head>
<meta charset="utf-8">
<title>BrineRun Business Card</title>
<link href="https://fonts.googleapis.com/css2?family=Source+Sans+3:wght@400;600&family=Arimo:wght@400&display=swap" rel="stylesheet">
<style>
  :root {
    --backdrop: #3a3a3a;
    --ocean: #0b93d1;
    --ocean-soft: #159cd8;
    --label: #8fd0f0;
    --paper: #ffffff;
  }
  * { margin: 0; padding: 0; box-sizing: border-box; }
  html, body { width: 1200px; height: 900px; overflow: hidden; }
  body { background: var(--backdrop); position: relative; font-family: "Arimo", Arial, sans-serif; }

  .card { position: absolute; top: 300px; width: 525px; height: 300px; overflow: hidden; }
  .card-front { left: 67px; background: var(--paper); }
  .card-back { left: 617px; background: var(--ocean); }
  .card svg.band { position: absolute; left: 0; top: 0; width: 525px; height: 300px; }

  .brand { position: absolute; left: 0; right: 0; top: 84px; text-align: center; color: var(--ocean);
           font-family: "Source Sans 3", sans-serif; }
  .brand-name { font-size: 80px; line-height: 80px; font-weight: 400; letter-spacing: -1px; }
  .brand-tagline { font-size: 25px; line-height: 28px; font-weight: 600; margin-top: 2px; }

  .logo-box { position: absolute; left: 31px; top: 68px; width: 225px; height: 159px; background: var(--ocean-soft);
              display: flex; align-items: center; justify-content: center; gap: 10px; }
  .logo-box .dot { width: 14px; height: 14px; border-radius: 50%; background: var(--paper); }
  .logo-box .logo-name { color: var(--paper); font-family: "Source Sans 3", sans-serif; font-weight: 400; font-size: 36px; }

  .contact { position: absolute; left: 275px; top: 108px; width: 250px; color: var(--paper); }
  .contact-name { font-size: 18px; padding-left: 1px; }
  .contact-role { font-size: 12px; margin-left: 6px; }
  .contact-rule { height: 2px; background: var(--paper); margin: 4px 0 7px; }
  .contact-line { font-size: 12.5px; line-height: 19px; padding-left: 1px; }
  .contact-line span { color: var(--label); }
</style>
</head>
<body>
  <section class="card card-front">
    <div class="brand">
      <div class="brand-name">BrineRun</div>
      <div class="brand-tagline">Ocean Water Supply</div>
    </div>
    <svg class="band" viewBox="0 0 525 300" aria-hidden="true">
      <path fill="var(--ocean)" d="M0,275 C110,245 220,240 300,262 C380,282 460,270 525,255 L525,300 L0,300 Z"/>
    </svg>
  </section>

  <section class="card card-back">
    <div class="logo-box">
      <span class="dot"></span>
      <span class="logo-name">BrineRun</span>
    </div>
    <div class="contact">
      <div><span class="contact-name">Dana Whitfield</span><span class="contact-role">Manager</span></div>
      <div class="contact-rule"></div>
      <div class="contact-line"><span>E:</span> info@brinerun.com.au</div>
      <div class="contact-line"><span>P:</span> +61400555012</div>
      <div class="contact-line"><span>W:</span> www.brinerun.com.au</div>
    </div>
    <svg class="band" viewBox="0 0 525 300" aria-hidden="true">
      <path fill="var(--paper)" d="M0,290 C90,262 200,258 290,268 C380,278 450,262 525,272 L525,300 L0,300 Z"/>
    </svg>
  </section>
</body>
</html>
```